Animal Horse & Bedding Company Needs a Website Coded & Designed

We need a website for a new animal bedding and feed company that is visually grabbing and vibrant. We would like to see a website that displays trust, quality and confidence. Needs to be responsive and mobile friendly for all browsers and coded for both Android & IOS. SEO is also important.

Joomla or Wordpress – must be both desktop and mobile friendly with fast page load speed. Need the ability to edit ourselves in Wordpress or Joomla.

Full details attached below with some layout and content ideas.

Coding

Coded - Design and coding required

Number of Pages Required

5+ page

Font styles to use
Sans Serif

Requirements
Must have
• Needs to be responsive and mobile friendly for all browsers and coded for both Android & IOS. SEO is also important.

Wordpress – must be both desktop and mobile friendly with fast page load speed. Need the ability to edit ourselves in Wordpress.

Logo Colours:
Dark Brown
CMYK: 50 / 70 / 80 / 70
Pantone: 4625C

Orange
CMYK: 0 / 50 / 100 / 0
Pantone: 144C
Nice to have
• Use picture of building attached and super impose logo on building.

```html
<!DOCTYPE html>
<html lang="en">
<head>
<meta charset="utf-8">
<title>The Tall Meadow – Horse Feed &amp; Bedding</title>
<link href="https://fonts.googleapis.com/css2?family=Open+Sans:wght@400;600;700&family=Montserrat:wght@600;700&display=swap" rel="stylesheet">
<style>
:root{
  --brown:#3a2415;
  --brown-deep:#2a190e;
  --orange:#f7941d;
  --cream:#ffffff;
  --grey:#f1f0ee;
  --text:#4a4a4a;
  --muted:#8a8580;
  --light:#e5d9cc;
}
*{box-sizing:border-box;margin:0;padding:0}
html,body{width:1200px;height:2656px;overflow:hidden}
body{font-family:"Open Sans",Arial,sans-serif;color:var(--text);background:var(--cream);position:relative;font-size:13px;line-height:1.6}
h1,h2,h3,h4{font-family:"Montserrat","Open Sans",sans-serif;font-weight:700}
.abs{position:absolute}
ul{list-style:none}

/* header */
.hero{position:absolute;left:0;top:0;width:1200px;height:560px;background:linear-gradient(180deg,#6b7d8f 0%,#8a9aa3 28%,#a04a3a 52%,#7a3a2c 64%,#556b3a 78%,#3f5230 100%)}
.hero-shade{position:absolute;inset:0;background:linear-gradient(180deg,rgba(20,12,6,.75) 0%,rgba(20,12,6,.35) 20%,rgba(20,12,6,.25) 60%,rgba(20,12,6,.55) 100%)}
.topbar{position:absolute;top:0;left:0;width:1200px;height:28px;display:flex;justify-content:center;gap:40px;align-items:center;color:#e8dccf;font-size:12px}
.topbar span{display:flex;align-items:center;gap:6px}
.nav{position:absolute;top:36px;left:520px;display:flex;gap:8px;align-items:center}
.nav a{color:#fff;text-decoration:none;font-weight:600;font-size:13px;padding:6px 14px;border-radius:14px}
.nav a.active{background:var(--orange)}
.nav a.quote{background:var(--orange);border-radius:3px;margin-left:10px;padding:7px 18px}
.brand{position:absolute;left:30px;top:38px;display:flex;align-items:center;gap:10px}
.brand-dot{width:14px;height:14px;border-radius:50%;background:var(--orange);flex:none}
.brand-name{font-family:"Open Sans",sans-serif;font-weight:700;color:#fff;font-size:17px;white-space:nowrap}
.hero-title{position:absolute;top:250px;left:0;width:1200px;text-align:center;color:#fff;font-size:28px;line-height:1.35;font-weight:600;text-shadow:0 2px 6px rgba(0,0,0,.45)}
.btn{display:inline-block;background:var(--orange);color:#fff;font-weight:600;font-size:12px;padding:7px 22px;border-radius:18px;text-decoration:none}
.hero-btn{position:absolute;top:342px;left:0;width:1200px;text-align:center}

/* features */
.features{position:absolute;top:520px;left:0;width:1200px;height:120px;background:var(--brown)}
.feature{position:absolute;top:26px;width:300px;display:flex;gap:12px;color:#e9ddd0}
.feature svg{flex:none}
.feature h4{color:var(--orange);font-size:13px;margin-bottom:2px}
.feature p{font-size:11px;line-height:1.5}

/* about */
.photo{position:absolute}
.section-title{font-size:26px;color:var(--brown);margin-bottom:14px}
.body-copy{font-size:12px;line-height:1.75;color:var(--text);margin-bottom:12px}
.btn-outline{display:inline-block;border:1px solid #9a9088;color:var(--brown);font-size:11px;font-weight:600;padding:5px 18px;border-radius:16px}
.values{display:flex;gap:34px;margin:8px 0 22px;font-size:12px;font-weight:600;color:var(--brown)}
.values span{display:flex;align-items:center;gap:8px}

/* feed */
.feed{position:absolute;top:1040px;left:0;width:1200px;height:520px;background:var(--brown)}
.feed-photo{position:absolute;right:0;top:0;width:600px;height:520px;background:linear-gradient(110deg,#4a2e1a 0%,#8a5a32 35%,#b8874e 55%,#6a4526 100%)}
.feed-copy{position:absolute;left:180px;top:72px;width:400px;color:var(--light)}
.feed-copy h2{color:var(--orange);font-size:26px;margin-bottom:12px}
.feed-copy h3{color:var(--orange);font-size:17px;margin:10px 0 8px}
.benefits{columns:2;column-gap:24px;font-size:11px}
.benefits li{display:flex;gap:8px;align-items:flex-start;margin-bottom:6px;break-inside:avoid}
.tick{flex:none;width:11px;height:11px;border:1px solid currentColor;margin-top:3px}
.feed .btn-outline{color:var(--light);border-color:#c9b9a8;margin-top:18px}

/* bedding */
.bedding-copy{position:absolute;left:580px;top:1610px;width:400px}
.bedding-copy h3{font-size:17px;color:var(--brown);margin:4px 0 8px}
.bedding-list li{display:flex;gap:8px;font-size:11px;margin-bottom:5px;color:var(--text)}

/* inquiry */
.inquiry{position:absolute;top:2040px;left:0;width:1200px;height:320px;background:var(--grey)}
.inquiry h2{text-align:center;font-size:26px;color:var(--brown);margin-top:40px}
.field{position:absolute;height:30px;background:#fff;border:1px solid #ddd;font-size:11px;color:var(--muted);padding:6px 10px;display:flex;align-items:center}
.field.msg{height:86px;align-items:flex-start}

/* footer */
.footer{position:absolute;top:2360px;left:0;width:1200px;height:266px;background:var(--brown)}
.footer h4{color:var(--orange);font-size:15px;margin-bottom:12px}
.fcol{position:absolute;top:52px;color:#dccfc1;font-size:12px}
.fcol li{margin-bottom:5px;display:flex;gap:8px;align-items:center}
.footer-brand{display:flex;align-items:center;gap:8px;margin-bottom:10px}
.footer-brand .brand-name{font-size:14px}
.socials{display:flex;gap:8px;margin-top:12px}
.socials i{width:22px;height:22px;border-radius:50%;background:#fff;display:block}
.copyright{position:absolute;top:2626px;left:0;width:1200px;height:30px;background:var(--orange);color:#fff;font-size:11px;text-align:center;line-height:30px}
</style>
</head>
<body>

<section class="hero">
  <div role="img" aria-label="Aerial photograph of red stable buildings and paddocks" style="position:absolute;inset:0"></div>
  <div class="hero-shade"></div>
</section>

<div class="topbar">
  <span><svg width="12" height="12" viewBox="0 0 24 24"><path fill="#f7941d" d="M6.6 10.8a15 15 0 0 0 6.6 6.6l2.2-2.2c.3-.3.7-.4 1-.2 1.1.4 2.3.6 3.6.6.6 0 1 .4 1 1V20c0 .6-.4 1-1 1A17 17 0 0 1 3 4c0-.6.4-1 1-1h3.5c.6 0 1 .4 1 1 0 1.3.2 2.5.6 3.6.1.3 0 .7-.2 1z"/></svg>(01234) 567 890</span>
  <span><svg width="13" height="11" viewBox="0 0 24 18"><rect x="1" y="1" width="22" height="16" fill="none" stroke="#f7941d" stroke-width="2"/><path d="M1 1l11 9 11-9" fill="none" stroke="#f7941d" stroke-width="2"/></svg>hello@tallmeadow.example</span>
</div>

<div class="brand"><span class="brand-dot"></span><span class="brand-name">The Tall Meadow</span></div>

<nav class="nav">
  <a class="active">Home</a><a>About</a><a>Feed</a><a>Bedding</a><a>Contact Us</a><a class="quote">Request Quote</a>
</nav>

<h1 class="hero-title">We are dedicated in providing high<br>quality products and services.</h1>
<div class="hero-btn"><span class="btn">Contact Us</span></div>

<section class="features">
  <div class="feature" style="left:170px">
    <svg width="30" height="30" viewBox="0 0 24 24"><path fill="#f7941d" d="M12 2l2.6 5.3 5.9.9-4.3 4.1 1 5.8L12 15.4 6.8 18.1l1-5.8L3.5 8.2l5.9-.9z"/></svg>
    <div><h4>Quality Guaranteed</h4><p>Every bale is graded for quality, dust-free and ready to use.</p></div>
  </div>
  <div class="feature" style="left:470px">
    <svg width="30" height="30" viewBox="0 0 24 24"><circle cx="12" cy="9" r="6" fill="none" stroke="#f7941d" stroke-width="2"/><path d="M9 15h6v5H9z" fill="#f7941d"/></svg>
    <div><h4>Full Service Solution</h4><p>From ordering to delivery, we handle every step for your stable.</p></div>
  </div>
  <div class="feature" style="left:770px">
    <svg width="30" height="30" viewBox="0 0 24 24"><circle cx="12" cy="12" r="9" fill="none" stroke="#f7941d" stroke-width="2"/><path d="M12 6v12M9 9h5a2 2 0 0 1 0 4h-4a2 2 0 0 0 0 4h5" fill="none" stroke="#f7941d" stroke-width="1.8"/></svg>
    <div><h4>Convenient &amp; Cost Effective</h4><p>Competitive prices with flexible delivery options to suit your yard.</p></div>
  </div>
</section>
<svg class="abs" style="top:636px;left:0" width="1200" height="50" viewBox="0 0 1200 50" preserveAspectRatio="none"><path d="M0 0H1200V10C900 50 600 30 300 14 180 8 80 14 0 24Z" fill="#3a2415"/></svg>

<div class="photo" role="img" aria-label="Photograph of two horses eating hay in a wooded paddock" style="left:180px;top:720px;width:290px;height:245px;background:linear-gradient(135deg,#8a6a45 0%,#4a3220 45%,#b59a6c 100%)"></div>
<div class="abs" style="left:500px;top:730px;width:420px">
  <h2 class="section-title">About Us</h2>
  <p class="body-copy">The Tall Meadow is a locally owned company based in the countryside. We are dedicated to providing high quality products and services.</p>
  <p class="body-copy">Producing, buying and distributing horse feed and bedding for over a decade of steady growth, backed by a trusted network of local suppliers.</p>
  <div class="values">
    <span><svg width="16" height="16" viewBox="0 0 24 24"><path fill="#f7941d" d="M12 2l8 3v6c0 5-3.5 9-8 11-4.5-2-8-6-8-11V5z"/></svg>Trust</span>
    <span><svg width="16" height="16" viewBox="0 0 24 24"><circle cx="12" cy="12" r="9" fill="#f7941d"/><path d="M8 12l3 3 5-6" stroke="#fff" stroke-width="2" fill="none"/></svg>Quality</span>
    <span><svg width="16" height="16" viewBox="0 0 24 24"><path fill="#f7941d" d="M12 2l2.6 5.3 5.9.9-4.3 4.1 1 5.8L12 15.4 6.8 18.1l1-5.8L3.5 8.2l5.9-.9z"/></svg>Confidence</span>
  </div>
  <span class="btn-outline">Read More ›</span>
</div>

<svg class="abs" style="top:1010px;left:0" width="1200" height="32" viewBox="0 0 1200 32" preserveAspectRatio="none"><path d="M0 32V14C300 -4 700 30 1200 6V32Z" fill="#3a2415"/></svg>
<section class="feed">
  <div class="feed-photo" role="img" aria-label="Photograph of a woman in a checked shirt feeding hay to a chestnut horse"></div>
  <div class="abs" style="left:0;top:0;width:700px;height:520px;background:linear-gradient(90deg,var(--brown) 80%,rgba(58,36,21,0))"></div>
  <div class="feed-copy">
    <h2>Feed</h2>
    <p class="body-copy" style="color:var(--light)">Our feed and bedding are sourced from trusted growers and tested for consistency, so your horses receive the nutrition and comfort they need every day.</p>
    <h3>Benefits</h3>
    <ul class="benefits">
      <li><i class="tick"></i>100% Natural</li>
      <li><i class="tick"></i>Chemical &amp; Additive Free</li>
      <li><i class="tick"></i>Suitable for Horses &amp; Ponies</li>
      <li><i class="tick"></i>High Protein Content</li>
      <li><i class="tick"></i>Consistent Mixed Formula</li>
      <li><i class="tick"></i>Clean – Dust Extracted</li>
      <li><i class="tick"></i>Low Starch</li>
      <li><i class="tick"></i>Easily Digested</li>
      <li><i class="tick"></i>Locally Harvested</li>
    </ul>
    <span class="btn-outline">Read More ›</span>
  </div>
</section>
<svg class="abs" style="top:1558px;left:0" width="1200" height="34" viewBox="0 0 1200 34" preserveAspectRatio="none"><path d="M0 0H1200V8C800 40 400 4 0 26Z" fill="#3a2415"/></svg>

<div class="photo" role="img" aria-label="Photograph of horses looking out from stable stalls" style="left:180px;top:1600px;width:290px;height:360px;background:linear-gradient(160deg,#c58a4a 0%,#6a4428 40%,#3a2616 70%,#8a6a48 100%)"></div>
<div class="bedding-copy">
  <h2 class="section-title" style="margin-bottom:6px">Bedding</h2>
  <p class="body-copy" style="margin-bottom:4px">Clean, dry and natural bedding.</p>
  <p class="body-copy">Our shavings are absorbent, low in dust and easy to muck out, keeping stables fresh for longer with less waste each week.</p>
  <h3>Benefits</h3>
  <ul class="bedding-list">
    <li><i class="tick"></i>100% Natural Chopped Straw</li>
    <li><i class="tick"></i>Low Dust</li>
    <li><i class="tick"></i>Chemical &amp; Additive Free</li>
    <li><i class="tick"></i>Clean &amp; Highly Absorbent</li>
    <li><i class="tick"></i>Cheaper than Wood Shavings</li>
    <li><i class="tick"></i>Premium – Burn and Rot Quickly</li>
    <li><i class="tick"></i>Environmentally Friendly – Recyclable &amp; Compostable</li>
  </ul>
  <span class="btn-outline" style="margin-top:14px">Read More ›</span>
</div>

<section class="inquiry">
  <h2>Quick Inquiry</h2>
  <div class="field" style="left:230px;top:110px;width:240px">Name</div>
  <div class="field" style="left:480px;top:110px;width:240px">Email</div>
  <div class="field" style="left:730px;top:110px;width:240px">Phone</div>
  <div class="field msg" style="left:230px;top:150px;width:740px">Your message</div>
  <div class="abs" style="left:0;top:258px;width:1200px;text-align:center"><span class="btn" style="background:var(--brown)">Submit ›</span></div>
</section>

<footer class="footer">
  <div class="fcol" style="left:180px;top:40px;width:200px">
    <div class="footer-brand"><span class="brand-dot"></span><span class="brand-name">The Tall Meadow</span></div>
    <p>Quality horse feed and bedding delivered to your door.</p>
    <div class="socials"><i></i><i></i><i></i><i></i></div>
  </div>
  <div class="fcol" style="left:400px">
    <h4>Quick Link</h4>
    <ul><li>› Home</li><li>› About</li><li>› Feed</li><li>› Bedding</li><li>› Contact Us</li></ul>
  </div>
  <div class="fcol" style="left:565px;width:200px">
    <h4>Contact Info</h4>
    <ul>
      <li style="align-items:flex-start"><svg width="12" height="14" viewBox="0 0 24 28" style="flex:none;margin-top:3px"><path fill="#f7941d" d="M12 0a9 9 0 0 1 9 9c0 7-9 19-9 19S3 16 3 9a9 9 0 0 1 9-9zm0 5a4 4 0 1 0 0 8 4 4 0 0 0 0-8z"/></svg>12 Meadow Lane, Ashford Green, AB1 2CD</li>
      <li><svg width="12" height="12" viewBox="0 0 24 24"><path fill="#f7941d" d="M6.6 10.8a15 15 0 0 0 6.6 6.6l2.2-2.2c.3-.3.7-.4 1-.2 1.1.4 2.3.6 3.6.6.6 0 1 .4 1 1V20c0 .6-.4 1-1 1A17 17 0 0 1 3 4c0-.6.4-1 1-1h3.5c.6 0 1 .4 1 1 0 1.3.2 2.5.6 3.6.1.3 0 .7-.2 1z"/></svg>(01234) 567 890</li>
      <li><svg width="12" height="10" viewBox="0 0 24 18"><rect x="1" y="1" width="22" height="16" fill="none" stroke="#f7941d" stroke-width="2"/><path d="M1 1l11 9 11-9" fill="none" stroke="#f7941d" stroke-width="2"/></svg>hello@tallmeadow.example</li>
    </ul>
  </div>
  <div class="fcol" style="left:790px;width:240px">
    <h4>Join Our Newsletter</h4>
    <div style="background:#fff;height:28px;border-radius:2px;color:var(--muted);font-size:11px;padding:6px 10px;margin-bottom:12px">Email address</div>
    <span class="btn" style="border-radius:3px">Subscribe Now</span>
  </div>
</footer>
<div class="copyright">Copyright © 2024 The Tall Meadow. All rights reserved.</div>

</body>
</html>
```